Bref créative
brochure and folder for a4 brochures
Brush Wave
Protecting your assets
Need a brochure template to use for Strata painting and residential painting
"STRATA BROCHURE COPY"
Brush Wave, the easy choice for strata paint works
Why strata managers love Brush Wave
Work with a company that focuses on your needs – a company that can get your strata painting works done with no hassle. We’ve been in business for over 20 years; we’re your one-stop shop for painting and remedial maintenance, and we get it right the first time.
At Brush Wave, we understand you need:
• Quality painting, project managed by us so you don’t have to take endless phone calls
• Great-value price: We take time to make sure of this
• Great ideas for colour schemes (saving the owners up to $700)
• Remedial repairs overseen by a qualified master builder
Why choose Brush Wave?
The Brush Wave difference means we turn up when we’re supposed to and finish on schedule. All our tradespeople are friendly, professional – and we promise that your site will be cleaner when we’ve finished than when we started.
Once you’ve accepted our quote, we can start within 24 hours and we manage the job from start to finish. You’ll be a hero with owners and you have peace of mind knowing the job’s under control.
Life’s easier with Brush Wave
Take the headache out of your strata painting works. Call Brush Wave on 1300 482 915.
What clients say about us
“Derek and his team have skilfully and professionally painted our property comprising 17 apartments and townhouses. The progress of the work has been clean and efficient and the result is excellent.”
Owen Falkirk, Moorings, Henley
“Communication is the key to successfully managing a project and Derek and his team exceeded expectations with updates concerning all aspects of the work.“ Neil Barker, Randwick
Add value to your new home before you move in, with Brush Wave
"RESIDENTIAL BROCHURE"
Start your new life with a clean freshly painted house
We’ve been in business for over 20 years and we know that when you move into your new home, it’s best to do all the basics first – quickly, with no fuss.
At Brush Wave, we understand you want:
• Quick, clean work: We can start within 24 hours and be in and out before you know it
• Good value: We also make remedial repairs so you get a perfect finish
• Great ideas for colour schemes (saving you up to $700)
• Friendly professional tradies you’ll be happy to have around your home
We turn up when we’re supposed to and finish on time. We’ll quote as soon as you pick up the keys and can advise on colours that will create just the right atmosphere. What’s more, your new home will be cleaner than when we started.
We guarantee
• Great-value price: We’ll help you make sure of this
• Impressive service: Fast, clean, quality job, and responsive to your needs
For feel-good factor, there’s nothing like a fresh splash of colour
If you’d like to start fresh, call Brush Wave on 1300 482 915.
"When dealing with Brush Wave we were given expert and professional advice in choosing colours for our beach house... The end result was great." Fiona Darrowby
Real Estate
corporate FOR STRATA
professional FOR RESIDENTIAL
need one brochure for residential painting and one for strata painting and a folder that we can use for both brochures
please use logo only do not use NSW or website under logo
please see attachment
please only use brushwave not background, lines or website under logo
another log for your use

```html
<!DOCTYPE html>
<html lang="en">
<head>
<meta charset="utf-8">
<title>Brush Wave – Brochure and Folder</title>
<link rel="stylesheet" href="https://fonts.googleapis.com/css2?family=Oswald:wght@400;600&family=Open+Sans:wght@400;600;700&display=swap">
<style>
  :root{
    --bg:#efe9e1;
    --navy:#1c2a38;
    --orange:#f2a21c;
    --paper:#ffffff;
    --ink:#3b4450;
    --sky-top:#9fb7cf;
    --sky-low:#5d7890;
    --faint:#eef1f5;
  }
  *{box-sizing:border-box;margin:0;padding:0}
  html,body{width:1200px;height:439px;overflow:hidden;background:var(--bg)}
  body{position:relative;font-family:"Open Sans",sans-serif}

  .photo{position:absolute;background:linear-gradient(180deg,var(--sky-top) 0%,#7d97ae 45%,var(--sky-low) 70%,#3f5a70 100%)}

  /* insert sheet */
  .insert{position:absolute;left:67px;top:65px;width:192px;height:326px;background:var(--paper);box-shadow:0 2px 6px rgba(0,0,0,.25);overflow:hidden}
  .insert .photo{left:0;top:0;width:100%;height:54px}
  .insert-title{position:absolute;left:0;top:54px;width:100%;height:30px;background:var(--navy);color:#fff;font-size:7px;font-weight:600;padding:6px 10px;line-height:1.35}
  .insert-title span{display:block;color:var(--orange);font-size:5.5px;font-weight:400}
  .insert-body{position:absolute;left:10px;top:90px;right:10px;font-size:4.6px;line-height:1.5;color:var(--ink)}
  .insert-body h4{font-size:5px;color:var(--navy);margin:5px 0 2px}
  .insert-body p{margin-bottom:3px}
  .insert-foot{position:absolute;left:0;bottom:0;width:100%;height:14px;background:var(--navy);color:#fff;font-size:4.5px;padding:4px 10px}

  /* front cover */
  .cover{position:absolute;left:295px;top:65px;width:413px;height:326px;background:var(--paper);box-shadow:0 2px 6px rgba(0,0,0,.25);overflow:hidden;z-index:1}
  .cover .photo{left:0;top:0;width:100%;height:100%}
  .cover-corner{position:absolute;left:0;top:0;width:100%;height:100%}
  .cover-headline{position:absolute;right:18px;top:20px;text-align:right;font-family:"Oswald",sans-serif;font-weight:600;color:var(--orange);font-size:16px;line-height:1.25;letter-spacing:.3px}
  .cover-you{position:absolute;left:226px;top:244px;font-family:"Oswald",sans-serif;font-weight:600;color:var(--orange);font-size:17px}
  .cover-logo{position:absolute;right:14px;top:282px}

  /* card pocket, sits in front of the cover */
  .card-pocket{position:absolute;left:276px;top:340px;width:176px;height:80px;background:var(--navy);border-radius:10px 10px 0 0;box-shadow:0 2px 5px rgba(0,0,0,.3);display:flex;align-items:center;justify-content:center;z-index:2}

  /* inside folder */
  .inside{position:absolute;left:720px;top:65px;width:408px;height:326px;background:var(--paper);box-shadow:0 2px 6px rgba(0,0,0,.25);overflow:hidden}
  .inside-paint{position:absolute;right:0;top:0;width:250px;height:210px;background:radial-gradient(ellipse at 80% 20%,#dfe4ec 0%,var(--faint) 45%,rgba(255,255,255,0) 75%)}
  .pocket{position:absolute;right:0;bottom:0;width:192px;height:108px;background:var(--navy);border-radius:18px 0 0 0;display:flex;align-items:center;justify-content:center}

  .brand{display:inline-flex;align-items:center;gap:5px;font-family:"Oswald",sans-serif;font-weight:600;font-size:16px;color:#fff;letter-spacing:.5px;white-space:nowrap}
  .brand i{display:block;width:9px;height:9px;border-radius:50%;background:var(--orange)}
  .brand.on-light{color:var(--navy)}
</style>
</head>
<body>

  <section class="insert">
    <div class="photo" role="img" aria-label="City harbour skyline photograph"></div>
    <div class="insert-title">Brush Wave, the easy choice for strata paint works
      <span>Why strata managers love Brush Wave</span></div>
    <div class="insert-body">
      <p>Work with a company that focuses on your needs – a company that gets your strata painting done with no hassle. We've been in business for over 20 years.</p>
      <h4>At Brush Wave, we understand you need:</h4>
      <p>• Quality painting, project managed by us<br>• Great-value price<br>• Great ideas for colour schemes<br>• Remedial repairs by a master builder</p>
      <h4>Why choose Brush Wave?</h4>
      <p>We turn up when we're supposed to and finish on schedule. Our tradespeople are friendly and professional, and your site will be cleaner when we finish.</p>
      <h4>Life's easier with Brush Wave</h4>
      <p>Take the headache out of your strata painting works. Call Brush Wave on 1300 482 915.</p>
      <h4>What clients say about us</h4>
      <p>"Derek and his team have skilfully and professionally painted our property." – Owen Falkirk, Moorings</p>
    </div>
    <div class="insert-foot">Call 1300 482 915</div>
  </section>

  <section class="cover">
    <div class="photo" role="img" aria-label="Aerial photograph of the city harbour and skyline"></div>
    <svg class="cover-corner" viewBox="0 0 413 326" aria-hidden="true">
      <polygon points="180,326 413,262 413,326" fill="#ffffff"/>
    </svg>
    <h1 class="cover-headline">SYDNEYS FAVORITE PAINTING FIRM<br>BY FOCUSING WHATS IMPORTANT</h1>
    <div class="cover-you">"YOU"</div>
    <div class="cover-logo"><span class="brand on-light">Brush Wave<i></i></span></div>
  </section>

  <div class="card-pocket"><span class="brand">Brush Wave<i></i></span></div>

  <section class="inside">
    <div class="inside-paint" role="img" aria-label="Faint photograph of open paint tins"></div>
    <div class="pocket"><span class="brand">Brush Wave<i></i></span></div>
  </section>

</body>
</html>
```